Stationery Design Project for High End Wealth Management Firm

We need a stationery design for our high-end wealth management firm. Our clientele are affluent and our brand is built around providing investment services with world-class service.

The final concepts should provide a business card, letterhead, and envelope.

We like the idea of having text on the front and back and we MUST have black front and back business cards.
For the business card we have the following that needs to be included:
Company Logo & Tagline
Employee Name
Employee title
Employee Email
Website
2 seperate office cities, addresses, and phone numbers
Financial disclosure (small print)

Having black envelopes would be neat, but black is not a must for the envelopes.
Updates

Project Deadline Extended
Reason: To give the concept one more day of revisions.

Project Deadline Extended
Reason: To allow for more concepts and designs.

Target Market(s)

High Net Worth

Industry/Entity Type

Business

Requirements
Must have
• The following disclosure must be on the back of the card in small print:

Investment Advisory Services offered through Harrowgate Asset Partners LLC, a SEC Registered Investment Advisor. Corvane Wealth Management LLC is not affiliated with Harrowgate Asset Partners LLC.

Black business cards are also a must have.

Please utilize each of the 3 components of our logo in the design.

Please use our white background logo elements when designing our letterhead if you need them.
Nice to have
• Please use our company colors when designing. Utilize a combination of the elements of our logo that we have attached.

We are going to be printing our business cards on letterpress.

```html
<!DOCTYPE html>
<html lang="en">
<head>
<meta charset="utf-8">
<title>Corvane Wealth Management – Stationery</title>
<link rel="stylesheet" href="https://fonts.googleapis.com/css2?family=Arimo:wght@400;700&display=swap">
<style>
  :root {
    --backdrop: #e4e2df;
    --paper: #ffffff;
    --card-black: #0b0b0b;
    --ink: #1e1e1e;
    --ink-soft: #555555;
    --gold: #c9954a;
    --web-orange: #b8651b;
    --faint-gold: #efe3d3;
  }
  * { margin: 0; padding: 0; box-sizing: border-box; }
  html, body { width: 1200px; height: 849px; overflow: hidden; }
  body {
    position: relative;
    background: var(--backdrop);
    font-family: "Arimo", Arial, sans-serif;
    color: var(--ink);
  }
  .sheet { position: absolute; }

  .brand-name {
    position: absolute;
    font-family: "Arimo", Arial, sans-serif;
    font-weight: 400;
    letter-spacing: 0.4px;
    white-space: nowrap;
  }
  .tagline { position: absolute; white-space: nowrap; }
  .website { position: absolute; font-weight: 700; color: var(--web-orange); white-space: nowrap; }

  /* letterhead */
  .letterhead { left: 565px; top: 40px; width: 593px; height: 768px; background: var(--paper); overflow: hidden; }
  .letterhead .brand-name { left: 38px; top: 52px; font-size: 13px; color: var(--ink); }
  .letterhead .tagline { left: 38px; top: 91px; font-size: 9.5px; color: var(--ink); }
  .letterhead .offices { position: absolute; right: 38px; top: 36px; text-align: right; font-size: 6px; line-height: 7.5px; color: var(--ink-soft); }
  .letterhead .offices p + p { margin-top: 7px; }
  .letterhead .website { right: 38px; top: 93px; font-size: 6px; }
  .letterhead .watermark { position: absolute; left: 330px; top: 420px; width: 300px; height: 300px; }

  /* business cards */
  .card { top: 198px; width: 244px; height: 140px; background: var(--card-black); color: #ffffff; overflow: hidden; }
  .card-front { left: 108px; }
  .card-back { left: 401px; }
  .card-front .brand-name { left: 12px; top: 17px; font-size: 7px; color: var(--gold); }
  .card-front .holder { position: absolute; left: 12px; top: 57px; font-size: 5px; line-height: 6.5px; color: #dddddd; }
  .card-front .holder-name { font-size: 7.5px; font-weight: 700; color: var(--gold); line-height: 9px; }
  .card-front .offices { position: absolute; left: 12px; top: 88px; font-size: 4.8px; line-height: 6.3px; color: #cccccc; }
  .card-front .offices p + p { margin-top: 4px; }
  .card-front .website { left: 12px; top: 123px; font-size: 4.8px; color: var(--gold); }
  .card-front .mark { position: absolute; left: 160px; top: 50px; }
  .card-back .brand-name { left: 35px; top: 40px; font-size: 10.5px; color: var(--gold); }
  .card-back .tagline { left: 35px; top: 79px; font-size: 7px; color: #ffffff; }
  .card-back .disclosure { position: absolute; left: 35px; top: 110px; width: 190px; font-size: 4.6px; line-height: 6px; color: #bbbbbb; }

  /* envelope */
  .envelope { left: 44px; top: 372px; width: 664px; height: 406px; }
  .envelope .flap { position: absolute; left: 0; top: 0; }
  .envelope .body { position: absolute; left: 0; top: 118px; width: 664px; height: 288px; background: var(--paper); overflow: hidden; }
  .envelope .body .brand-name { left: 31px; top: 38px; font-size: 11px; color: var(--ink); }
  .envelope .body .tagline { left: 31px; top: 74px; font-size: 8px; }
  .envelope .body .website { left: 31px; top: 249px; font-size: 6.5px; }
  .envelope .body .watermark { position: absolute; left: 500px; top: 100px; width: 220px; height: 220px; }
  .flap-address { position: absolute; top: 14px; font-size: 5.5px; line-height: 7px; color: #dddddd; transform: rotate(180deg); white-space: nowrap; }
  .flap-address.san-diego { right: 368px; text-align: left; }
  .flap-address.tucson { left: 346px; text-align: right; }
</style>
</head>
<body>

  <section class="sheet letterhead">
    <div class="brand-name">CORVANE WEALTH MANAGEMENT</div>
    <div class="tagline">Preferred Wealth Management for Select Individuals</div>
    <div class="offices">
      <p>4120 N Sagebrush Way<br>Tucson, AZ 85750<br>T (520) 555-0148</p>
      <p>2870 Harbor Ridge Drive, Suite 410<br>San Diego, CA 92121<br>T (858) 555-0193</p>
    </div>
    <div class="website">www.corvanewm.com</div>
    <svg class="watermark" viewBox="0 0 300 300" aria-hidden="true">
      <circle cx="150" cy="150" r="150" fill="var(--faint-gold)"/>
    </svg>
  </section>

  <section class="sheet card card-front">
    <div class="brand-name">CORVANE WEALTH MANAGEMENT</div>
    <div class="holder">
      <div class="holder-name">Daniel Reyes</div>
      Chief Executive Officer<br>
      daniel.reyes@corvanewm.com
    </div>
    <div class="offices">
      <p>4120 N Sagebrush Way, Tucson, AZ 85750<br>T (520) 555-0148</p>
      <p>2870 Harbor Ridge Dr, Suite 410, San Diego, CA 92121<br>T (858) 555-0193</p>
    </div>
    <div class="website">www.corvanewm.com</div>
    <svg class="mark" width="70" height="70" viewBox="0 0 70 70" aria-hidden="true">
      <circle cx="35" cy="35" r="33" fill="var(--gold)"/>
    </svg>
  </section>

  <section class="sheet card card-back">
    <div class="brand-name">CORVANE WEALTH MANAGEMENT</div>
    <div class="tagline">Preferred Wealth Management for Select Individuals</div>
    <p class="disclosure">Investment Advisory Services offered through Harrowgate Asset Partners LLC, a SEC Registered Investment Advisor. Corvane Wealth Management LLC is not affiliated with Harrowgate Asset Partners LLC.</p>
  </section>

  <section class="sheet envelope">
    <svg class="flap" width="664" height="119" viewBox="0 0 664 119" aria-hidden="true">
      <path d="M0 119 L22 0 L650 0 Q664 0 664 14 L664 119 Z" fill="var(--card-black)"/>
      <line x1="334" y1="6" x2="334" y2="30" stroke="var(--gold)" stroke-width="1"/>
      <circle cx="334" cy="76" r="14" fill="var(--gold)"/>
    </svg>
    <div class="flap-address san-diego">2870 Harbor Ridge Drive, Suite 410, San Diego, CA 92121<br>T (858) 555-0193</div>
    <div class="flap-address tucson">4120 N Sagebrush Way, Tucson, AZ 85750<br>T (520) 555-0148</div>
    <div class="body">
      <div class="brand-name">CORVANE WEALTH MANAGEMENT</div>
      <div class="tagline">Preferred Wealth Management for Select Individuals</div>
      <div class="website">www.corvanewm.com</div>
      <svg class="watermark" viewBox="0 0 220 220" aria-hidden="true">
        <circle cx="110" cy="110" r="110" fill="var(--faint-gold)"/>
      </svg>
    </div>
  </section>

</body>
</html>
```